Flyer/Poster design required for volunteer activities

We need a STRIKING A4 Poster/Flyer advertising our conservation volunteer program activities which are currently happening in the area. This poster is to advertise the program once people have arrived on the island or to locals. The program covers 5 months, May-September 2019 and is focused on conservation. I have attached the following:
- a flyer which was previously created (QMR Habitat Helpers 2019 sm)to advertise the program - would prefer it has a similar striking resemblance, but not essential
- A mock up document 'HHQMR On Island Poster_2019_v2' with text -Logos-Images

Target Market(s)

Everyone interested in Environmental Adventure/Hiking/Citizen Science

Industry/Entity Type

Tourism

Font styles to use
Sans Serif

Requirements
Must have
• -A travel conservation focus
• -Must use 'QMR-Background Image' as the background to the design
• -The info of where to get more information and the social media details must be prominent

```html
<!DOCTYPE html>
<html lang="en">
<head>
<meta charset="utf-8">
<title>QMR Habitat Helpers – Protecting Paradise 2019</title>
<link rel="stylesheet" href="https://fonts.googleapis.com/css2?family=Catamaran:wght@500;700;800&family=Nunito+Sans:wght@400;600;700&display=swap">
<style>
  :root {
    --yellow: #ffec00;
    --ink: #1b1d16;
    --white: #ffffff;
    --navy: #1f4a9a;
    --page: #e9e7e2;
    --jungle-dark: #14190f;
    --jungle-mid: #2c3a1e;
  }
  * { box-sizing: border-box; margin: 0; padding: 0; }
  html, body { width: 1200px; height: 1200px; overflow: hidden; background: var(--page); }
  .flyer {
    position: absolute; left: 200px; top: 34px; width: 800px; height: 1132px;
    overflow: hidden; background: var(--jungle-dark);
    font-family: "Nunito Sans", sans-serif; color: var(--white);
    box-shadow: 0 6px 24px rgba(0,0,0,.25);
  }
  .backdrop {
    position: absolute; inset: 0;
    background:
      linear-gradient(180deg,
        #b9c9da 0%, #dfe6ee 12%, #8fb0c8 22%, #4f8ea8 30%,
        #3f8a8f 36%, #5c7a45 44%, #4b5e31 52%,
        var(--jungle-mid) 62%, #1e2716 78%, var(--jungle-dark) 100%);
  }
  .swoosh { position: absolute; left: 0; top: 0; width: 800px; height: 700px; }
  .brand-badge {
    position: absolute; left: 28px; top: 22px; width: 150px; height: 150px;
    border-radius: 50%; background: var(--white);
    display: flex; align-items: center; justify-content: center; text-align: center;
    font-family: "Catamaran", sans-serif; font-weight: 800; color: var(--navy);
    font-size: 22px; line-height: 1.05; padding: 18px;
  }
  .tag {
    position: absolute; left: 0; top: 205px; height: 44px; padding: 0 18px 0 30px;
    background: var(--yellow); color: var(--ink);
    font-family: "Catamaran", sans-serif; font-weight: 500; font-size: 31px; line-height: 46px;
  }
  .place {
    position: absolute; left: 30px; top: 254px;
    font-family: "Catamaran", sans-serif; font-weight: 800; font-size: 44px; letter-spacing: 1px;
    text-shadow: 0 2px 6px rgba(0,0,0,.35);
  }
  .aerial {
    position: absolute; left: 32px; top: 325px; width: 170px; height: 170px; border-radius: 50%;
    border: 5px solid var(--yellow);
    background: radial-gradient(circle at 60% 35%, #6d8a55 0 18%, #3fb1c9 30%, #1f86a6 60%, #175d7a 100%);
  }
  .season {
    position: absolute; left: 225px; top: 372px;
    font-family: "Catamaran", sans-serif; font-weight: 800; font-size: 32px; color: var(--yellow);
    text-shadow: 0 2px 4px rgba(0,0,0,.4);
  }
  .focus {
    position: absolute; left: 232px; top: 414px;
    font-family: "Catamaran", sans-serif; font-weight: 700; font-size: 21px;
    text-shadow: 0 1px 4px rgba(0,0,0,.5);
  }
  .intro { position: absolute; left: 40px; top: 536px; right: 40px; }
  .intro-kicker { font-family: "Catamaran", sans-serif; font-weight: 800; font-size: 28px; line-height: 1; }
  .intro-title {
    font-family: "Catamaran", sans-serif; font-weight: 800; font-size: 37px; color: var(--yellow);
    line-height: 1.1; margin-top: 10px; white-space: nowrap;
  }
  .intro-lead {
    font-family: "Catamaran", sans-serif; font-weight: 500; font-size: 19px; color: var(--yellow);
    text-transform: uppercase; line-height: 1.1; margin-top: 8px;
  }
  .body-copy { margin-top: 14px; font-size: 14.2px; line-height: 1.3; text-align: justify; }
  .body-copy p + p { margin-top: 10px; }
  .quote { position: absolute; left: 40px; right: 40px; top: 872px; }
  .quote-line1 {
    font-family: "Catamaran", sans-serif; font-weight: 500; font-size: 28px; color: var(--yellow);
    padding-left: 30px; line-height: 1.1; position: relative;
  }
  .quote-line1::before { content: "\201C"; position: absolute; left: 0; top: -4px; color: var(--white); font-size: 30px; }
  .quote-line2 {
    font-family: "Catamaran", sans-serif; font-weight: 800; font-size: 27px;
    padding-left: 30px; line-height: 1.3; position: relative;
  }
  .quote-line2::after { content: "\201D"; position: absolute; right: 0; top: 10px; font-size: 30px; }
  .quote-author { text-align: right; font-size: 20px; margin-top: 14px; padding-right: 10px; }
  .contact-bar {
    position: absolute; left: 0; right: 0; bottom: 0; height: 128px; background: var(--yellow);
    display: grid; grid-template-columns: 1fr 1fr 1fr; align-items: center;
    color: var(--ink); font-family: "Catamaran", sans-serif; font-weight: 700; font-size: 18px;
  }
  .contact { display: flex; flex-direction: column; align-items: center; gap: 10px; height: 84px; justify-content: center; }
  .contact + .contact { border-left: 2px solid var(--ink); }
  .contact-icon { width: 34px; height: 34px; }
  .contact-mark { width: 30px; height: 30px; border: 3px solid var(--ink); border-radius: 50%; }
</style>
</head>
<body>
  <main class="flyer">
    <div class="backdrop" role="img" aria-label="Hiker with backpack on a clifftop overlooking a lagoon, beaches and green hills, fading into dense palm forest"></div>

    <svg class="swoosh" viewBox="0 0 800 700" aria-hidden="true">
      <path d="M0 420 C120 470 220 545 380 525 C560 505 700 420 800 270 L800 700 L0 700 Z" fill="rgba(15,20,10,.55)"/>
      <path d="M0 420 C120 470 220 545 380 525 C560 505 700 420 800 270" fill="none" stroke="#ffec00" stroke-width="13"/>
    </svg>

    <div class="brand-badge">QMR Habitat Helpers</div>

    <div class="tag">MAKE A DIFFERENCE</div>
    <h1 class="place">QUILL MARSH REACH</h1>

    <div class="aerial" role="img" aria-label="Aerial view of the island lagoon and reef"></div>

    <h2 class="season">PROTECTING PARADISE 2019</h2>
    <p class="focus">Conservation | Nature | Citizen Science</p>

    <section class="intro">
      <p class="intro-kicker">JOIN OUR</p>
      <h3 class="intro-title">QMR HABITAT HELPERS PROGRAM</h3>
      <p class="intro-lead">In 2019 and be involved in a world class, award winning holistic conservation effort – protecting paradise</p>
      <div class="body-copy">
        <p>Quill Marsh Reach and its surrounding marine park are located 600km off the Southern Cape coast and are renowned for their spectacular scenery. An important breeding ground for colonies of seabirds, the rich biodiversity of Quill Marsh Reach includes many endangered and critically endangered species found nowhere else in the world.</p>
        <p>The QMR Habitat Helpers program believe in protecting Quill Marsh Reach's unique biodiversity while showcasing world class conservation in action. We are dedicated to empowering like-minded people to make a difference through robust citizen science, inspiring educational experiences, and tangible local conservation.</p>
      </div>
    </section>

    <blockquote class="quote">
      <p class="quote-line1">QUILL MARSH REACH IS</p>
      <p class="quote-line2">SO EXTRAORDINARY IT IS ALMOST UNBELIEVABLE</p>
      <p class="quote-author">Dr Helena Marchetti</p>
    </blockquote>

    <footer class="contact-bar">
      <div class="contact">
        <svg class="contact-icon" viewBox="0 0 34 34" aria-hidden="true" fill="none" stroke="#1b1d16" stroke-width="2.4">
          <circle cx="17" cy="17" r="14"/>
          <ellipse cx="17" cy="17" rx="6" ry="14"/>
          <line x1="3" y1="17" x2="31" y2="17"/>
          <path d="M6 9 H28 M6 25 H28"/>
        </svg>
        <span>www.quillmarshreach.info</span>
      </div>
      <div class="contact">
        <span class="contact-mark"></span>
        <span>www.community.net/hhqmr</span>
      </div>
      <div class="contact">
        <span class="contact-mark"></span>
        <span>photos @hhqmr</span>
      </div>
    </footer>
  </main>
</body>
</html>
```